Web Design Project

We need the homepage and 7 interior pages designed as described below - design only:

Main Page
We like this template: http://www.layoutbarn.example/demo/52917.html

We also want a login dropdown similar to http://www.vortelle.example

We want the main page to be luxurious and sleek. We are a limo company that is dedicated to good service and creating an experience, and our front page should strongly reflect that. We do not want a very busy front page.

The main page should do primary things:

1. Make Reservations: We really like rideharbor.example for this aspect of the site. That being said, rideharbor is NOT the type of company we are.
2. Inform the customer of our most popular packages and give a sense of our professionalism and luxurious service.
3. There should be an area for a customer login
4. Menu should include the following: Home, Who We Are, Our Fleet, Custom Packages,
Testimonials, Book Your Ride!

For a starting point, we like this template http://www.layoutbarn.example/demo/52917.html

Rather than "start up, integrate, develop" we could have 3 of the more popular packages (or categories of packages). The bottom part would be fine. We could have a chirpline feed, welcome, and our core principles. The one big change would be the addition of a "booking" area right smack in the middle of the page, where a customer could enter in trip data and see if the date was available.

-

About Us - Secondary Page
We like this ABOUT page template: http://www.layoutbarn.example/demo/63824.html

This is a really important page that people overlook, yet it is the most viewed page of a website after the homepage. We have come up with a bit of text to go on the about us page:

Who We Are: Velvet Cars was founded on the core principle that every limo ride starts with personalized service from the instant you book your ride and continues after you step out of the car. You and your party are more than just our customers. We consider knowing your name and providing you with your choice of snacks and periodicals in the car just a few of the integral elements of the limousine experience. We are striving to revolutionize the limousine industry by creating a personal, friendly, timely, and professional experience. Velvet Cars combines current technology and a modern fleet with good old-fashioned service to deliver you a personalized, luxury experience. We cater to every event, from business travel to proms and wedding, and everything in between.

We do all of this while maintaining competitive pricing to our peers.

Have a taste of high society...

-

Custom Packages - Secondary Page

This page will contain descriptions of the packages that we offer: Wedding, Prom, Business, etc. - there should be a thumbnail of each package with a description next to it. When you click on a thumbnail it will bring you to a detailed page of that particular package.

-

Custom Packages Interior Page - Secondary Page

In depth look at that particular package - for example, weddings - shows that we offer complimentary champagne, Just married sign, etc.

-

Fleet Page - Secondary Page

This page can be fairly basic. It will include photos of the vehicles along with descriptions and number of passengers, etc.

-

Testimonials Page - Secondary Page

This page will have testimonials from customers. We don't want a big block of text, but rather small testimonials that will expand within the page when you click on a "+" symbol. We like the way it looks when the testimonials are enclosed within a speech bubble image - still professional and classy, not cheesy.

-

Book your ride! - Secondary Page

This page will have a form on it - the same as the form on the homepage, where people can enter in information to check the availability of vehicles. We also want basic contact information on this page as well in case people want to call directly or e-mail.

Requirements
Must have
• - Book your reservation form on homepage
- Sleek, elegant feel
- Chirpline feed

```html
<!DOCTYPE html>
<html lang="en">
<head>
<meta charset="utf-8">
<title>Velvet Cars</title>
<link rel="stylesheet" href="https://fonts.googleapis.com/css2?family=Raleway:wght@200;300;400&family=Questrial&family=Montserrat:wght@700&family=Arimo:wght@400;700&display=swap">
<style>
:root{
  --navy:#1c2553;
  --navy-light:#26336e;
  --body-bg:#23262f;
  --footer-bg:#1b2350;
  --accent-blue:#2b7fc4;
  --ribbon-blue:#0f56b0;
  --ribbon-dark:#0a3f86;
  --yellow:#f3d21b;
  --yellow-dark:#c9a90a;
  --text:#d9dbe2;
  --text-strong:#e8e9ee;
  --nav-btn:#1a2048;
  --form-top:#ffffff;
  --form-bottom:#9a9ca2;
  --rule:#b9bcc6;
}
*{box-sizing:border-box;margin:0;padding:0}
html,body{width:1091px;height:1200px;overflow:hidden}
body{position:relative;background:var(--body-bg);font-family:"Arimo",Arial,sans-serif;color:var(--text)}
.abs{position:absolute}

/* header */
.site-header{left:0;top:0;width:1091px;height:225px;background:linear-gradient(135deg,var(--navy) 0%,var(--navy-light) 45%,var(--navy) 100%)}
.login-tab{left:895px;top:0;width:76px;height:25px;background:#e4e6ec;color:#2a3470;font-family:"Questrial",sans-serif;font-size:14px;text-align:center;line-height:26px}
.brand{left:0;top:72px;width:1091px;text-align:center}
.brand-name{font-family:"Raleway",sans-serif;font-weight:300;font-size:32px;letter-spacing:4px;color:#fff}
.main-nav{left:109px;top:167px;display:flex;gap:14px}
.nav-item{width:134px;height:47px;background:var(--nav-btn);color:#e6e8f0;font-family:"Questrial",sans-serif;font-size:14px;display:flex;align-items:center;justify-content:center;text-align:center;line-height:17px}
.nav-item.is-active{background:linear-gradient(var(--yellow),var(--yellow-dark));color:#3a3510}

/* hero */
.hero-photo{left:109px;top:239px;width:579px;height:331px;background:radial-gradient(ellipse at 60% 70%,#2c2b22 0%,#14161a 60%,#0e1014 100%)}
.slogan{left:103px;top:486px;width:362px;height:50px;background:linear-gradient(var(--ribbon-blue),var(--ribbon-dark));clip-path:polygon(0 0,96% 0,100% 100%,0 100%);color:#fff;font-family:"Montserrat",sans-serif;font-weight:700;font-size:19px;letter-spacing:1.5px;line-height:50px;padding-left:21px}

/* booking form */
.booking{left:701px;top:239px;width:281px;height:331px;background:linear-gradient(var(--form-top) 0%,#dcdde0 50%,var(--form-bottom) 100%);color:#222;font-size:12.5px}
.radio-row{position:absolute;left:13px;top:16px;display:flex;gap:44px;align-items:center}
.radio{display:flex;align-items:center;gap:6px}
.radio-dot{width:13px;height:13px;border-radius:50%;border:1px solid #888;background:#fff;display:inline-block;position:relative}
.radio-dot.is-on::after{content:"";position:absolute;left:3px;top:3px;width:5px;height:5px;border-radius:50%;background:#111}
.booking-rule{position:absolute;left:13px;top:44px;width:255px;height:1px;background:#cfd0d4}
.field-label{position:absolute;left:13px}
.field{position:absolute;height:29px;background:#fff;border:1px solid #b8b9bd;font-size:11px;color:#666;line-height:27px;padding-left:9px}
.book-btn{right:-5px;top:248px;width:215px;height:50px;background:linear-gradient(var(--ribbon-blue),var(--ribbon-dark));clip-path:polygon(4% 0,100% 0,100% 100%,0 100%,0 0);color:#fff;font-family:"Questrial",sans-serif;font-size:21px;line-height:50px;text-align:center;padding-left:8px}

/* content */
.section-title{font-family:"Raleway",sans-serif;font-weight:300;font-size:29px;color:var(--accent-blue)}
.welcome{left:112px;top:594px;width:411px}
.lead{font-weight:700;font-size:12.7px;line-height:15.5px;color:var(--text-strong);margin-top:18px}
.body-copy{font-size:12.7px;line-height:15.5px;text-align:justify;margin-top:15px;color:var(--text)}
.principles{left:570px;top:594px;width:413px}
.principle{display:flex;align-items:flex-start;margin-top:14px}
.principle:first-of-type{margin-top:18px}
.principle-num{width:46px;font-family:"Arimo",sans-serif;font-weight:700;font-size:46px;line-height:46px;background:linear-gradient(#fff,#8e939e);-webkit-background-clip:text;background-clip:text;color:transparent}
.principle-text{border-left:1px solid #555a66;padding-left:17px;font-size:12.7px;line-height:15.5px;min-height:40px}
.divider{left:112px;top:837px;width:871px;height:1px;background:var(--rule)}
.packages-title{left:109px;top:855px}
.package{top:908px}
.package-head{display:flex;justify-content:space-between;font-family:"Raleway",sans-serif;font-weight:300;font-size:29px;color:#e6e8f0;padding-bottom:6px;border-bottom:1px solid var(--rule)}
.package.is-featured .package-head{border-bottom:2px solid var(--yellow)}
.package .lead{margin-top:15px;text-align:justify}
.package .body-copy{margin-top:14px}

/* footer */
.site-footer{left:0;top:1121px;width:1091px;height:79px;background:var(--footer-bg)}
.contact-title{left:114px;top:18px;font-family:"Raleway",sans-serif;font-weight:300;font-size:30px;color:#fff}
.contact-rule{left:279px;top:16px;width:1px;height:40px;background:#8a90a6}
.contact-copy{left:306px;top:22px;width:300px;font-size:12.7px;line-height:15.5px}
.social{left:841px;top:25px;display:flex;gap:10px}
.social-dot{width:31px;height:31px;border-radius:50%;background:#141a3a}
</style>
</head>
<body>

<header class="site-header abs">
  <div class="login-tab abs">LOG-IN</div>
  <div class="brand abs">
    <div class="brand-name">VELVET CARS</div>
  </div>
  <nav class="main-nav abs">
    <div class="nav-item is-active">HOME</div>
    <div class="nav-item">WHO WE ARE</div>
    <div class="nav-item">OUR FLEET</div>
    <div class="nav-item">CUSTOM<br>PACKAGES</div>
    <div class="nav-item">TESTIMONIALS</div>
    <div class="nav-item">BOOK<br>YOUR RIDE</div>
  </nav>
</header>

<div class="hero-photo abs" role="img" aria-label="Blurred night city skyline with scattered lights"></div>
<div class="slogan abs">A SLOGAN CAN GO HERE</div>

<form class="booking abs">
  <div class="radio-row">
    <span class="radio"><span class="radio-dot is-on"></span>One way</span>
    <span class="radio"><span class="radio-dot"></span>By the hour</span>
  </div>
  <div class="booking-rule"></div>
  <div class="field-label" style="top:62px">I want to be picked up at</div>
  <div class="field" style="left:13px;top:77px;width:255px">Enter Address, Airport or Landmark</div>
  <div class="field-label" style="top:124px">And dropped off at</div>
  <div class="field" style="left:13px;top:139px;width:255px">Enter Address, Airport or Landmark</div>
  <div class="field-label" style="top:185px">Pickup date</div>
  <div class="field-label" style="left:146px;top:185px">Pickup time</div>
  <div class="field" style="left:13px;top:200px;width:120px">22-10.2012
    <svg class="abs" style="right:7px;top:8px" width="12" height="11" viewBox="0 0 12 11"><rect x="3" y="0.5" width="8" height="6" fill="none" stroke="#2a4a8a"/><rect x="0.5" y="4" width="8" height="6" fill="#fff" stroke="#2a4a8a"/></svg>
  </div>
  <div class="field" style="left:146px;top:200px;width:120px">9:30 PM
    <svg class="abs" style="right:8px;top:10px" width="12" height="8" viewBox="0 0 12 8"><path d="M1 1l5 5 5-5" fill="none" stroke="#2a7fc4" stroke-width="2.5"/></svg>
  </div>
  <div class="book-btn abs">BOOK YOUR RIDE</div>
</form>

<section class="welcome abs">
  <h2 class="section-title">WELCOME</h2>
  <p class="lead">Lorem ipsum dolor sit amet, consectetur adipisicing elit. Proin nibh augue, suscipit a, scelerisque sed, lacinia in, mi. Cras vel lorem.</p>
  <p class="body-copy">Etiam pellentesque aliquetLorem ipsum dolor sit amet, consectetur adipisicing elit. Proin nibh augue, suscipit a, scelerisque sed, lacinia in, mi. Cras vel lorem. Etiam pellentesque aliquetLorem ipsum dolor sit amet, consectetur adipisicing elit. Proin nibh augue, suscipit a, scelerisque sed, lacinia in, mi. Cras vel lorem. Etiam pellentesque aliquetLorem ipsum dolor sit amet, consectetur adipisicing elit. Proin nibh augue, suscipit a, scelerisque sed, lacinia in, mi. Cras vel lorem. Etiam pellentesque m ipsum do aliquetiam pelle.</p>
</section>

<section class="principles abs">
  <h2 class="section-title">CORE PRINCIPLES</h2>
  <div class="principle"><span class="principle-num">1</span><p class="principle-text">Lorem ipsum dolor sit amet, consectetur adipisicing elit. Proin nibh augue, suscipit a, scelerisque sed, lacinia in, mi. Cras vel lorem. Etiam pellentesque aliquet</p></div>
  <div class="principle"><span class="principle-num">2</span><p class="principle-text">Scelerisque sed, lacinia in, mi. Cras vel lorem. Etiam pellentesque aliquetLorem ipsum dolor sit amet, consectetur adipisicing elit.</p></div>
  <div class="principle"><span class="principle-num">3</span><p class="principle-text">Proin nibh augue, suscipit a, scelerisque sed, lacinia in, mi. Cras vel lorem. Etiam pellentesque aliquet proin nibh augue, suscipit a, scelerisque sed, lacinia in, mi. Cras vel lorem.</p></div>
</section>

<div class="divider abs"></div>
<h2 class="section-title packages-title abs">POPULAR PACKAGES</h2>

<article class="package abs" style="left:109px;width:282px">
  <div class="package-head"><span>SILVER</span><span>$99</span></div>
  <p class="lead">Lorem ipsum dolor sit amet, consectetur adipisicing elit. Proin nibh augue, suscipit a, scelerisque sed, lacinia in, mi. Cras vel lorem.</p>
  <p class="body-copy">Etiam pellentesque aliquetLorem ipsum dolor sit amet, consectetur adipisicing elit.</p>
</article>
<article class="package is-featured abs" style="left:408px;width:279px">
  <div class="package-head"><span>GOLD</span><span>$299</span></div>
  <p class="lead">Lorem ipsum dolor sit amet, consectetur adipisicing elit. Proin nibh augue, suscipit a, scelerisque sed, lacinia in, mi. Cras vel lorem.</p>
  <p class="body-copy">Etiam pellentesque aliquetLorem ipsum dolor sit amet, consectetur adipisicing elit.</p>
</article>
<article class="package abs" style="left:707px;width:282px">
  <div class="package-head"><span>DIAMOND</span><span>$599</span></div>
  <p class="lead">Lorem ipsum dolor sit amet, consectetur adipisicing elit. Proin nibh augue, suscipit a, scelerisque sed, lacinia in, mi. Cras vel lorem.</p>
  <p class="body-copy">Etiam pellentesque aliquetLorem ipsum dolor sit amet, consectetur adipisicing elit.</p>
</article>

<footer class="site-footer abs">
  <h2 class="contact-title abs">CONTACT</h2>
  <div class="contact-rule abs"></div>
  <p class="contact-copy abs">Etiam pellentesque aliquetLorem ipsum dolor sit amet, consectetur adipisicing elit.</p>
  <div class="social abs" aria-label="Social links">
    <span class="social-dot"></span><span class="social-dot"></span><span class="social-dot"></span><span class="social-dot"></span>
  </div>
</footer>

</body>
</html>
```